Realtor/Real Estate Investor Business Card Design

We need a business card design for a new real estate company in Maryland. We buy houses, fix and sell. We do wholesaling as well. We also rent houses.We would like to have blue background and white font.
Updates

Hi All,
I thank all of you for your efforts. You are all experts in designing.
Looking forward to meeting you online in the near future.
mira

Industry/Entity Type

Real Estate

Contact Information for Business Card

Mira Talwen
Real Estate Professional
mira@brightkeyhomes.com
301-584-3092
Bright K Homes.com

Requirements
Must have
• House picture, and logo at the back of the card
We simplify your buying and selling real estate. at the back of the card

```html
<!DOCTYPE html>
<html lang="en">
<head>
<meta charset="utf-8">
<title>Mira Talwen – Business Card</title>
<link rel="stylesheet" href="https://fonts.googleapis.com/css2?family=Questrial&display=swap">
<style>
  :root {
    --page-bg: #ffffff;
    --navy: #1b2230;
    --navy-deep: #121824;
    --navy-mid: #242d3d;
    --silver-light: #f2f2f2;
    --silver: #c9ccd1;
    --silver-dark: #8d9299;
    --ink: #1d2a44;
    --white: #ffffff;
    --card-radius: 22px;
  }
  * { box-sizing: border-box; margin: 0; padding: 0; }
  html, body {
    width: 1200px;
    height: 900px;
    overflow: hidden;
    background: var(--page-bg);
    font-family: "Questrial", "Century Gothic", sans-serif;
  }
  .canvas {
    width: 1200px;
    height: 900px;
    display: flex;
    align-items: center;
    justify-content: center;
    gap: 60px;
  }
  .card {
    position: relative;
    width: 520px;
    height: 310px;
    border-radius: var(--card-radius);
    overflow: hidden;
    box-shadow: 0 10px 24px rgba(0, 0, 0, 0.18);
  }
  .brand-mark {
    display: block;
    border-radius: 3px;
  }

  /* Front side */
  .card-front {
    background: linear-gradient(180deg, var(--silver-light) 0%, var(--white) 55%);
  }
  .front-brand {
    position: absolute;
    top: 0;
    left: 0;
    right: 0;
    height: 178px;
    display: flex;
    flex-direction: column;
    align-items: center;
    justify-content: flex-start;
    padding-top: 30px;
  }
  .front-brand .brand-mark {
    width: 42px;
    height: 42px;
    background: var(--ink);
    margin-bottom: 12px;
  }
  .front-brand .brand-name {
    font-size: 38px;
    color: var(--ink);
    letter-spacing: 1px;
    line-height: 1;
  }
  .front-brand .brand-role {
    margin-top: 6px;
    font-size: 18px;
    color: var(--ink);
    letter-spacing: 0.5px;
  }
  .silver-band {
    position: absolute;
    top: 178px;
    left: 0;
    right: 0;
    height: 12px;
    background: linear-gradient(90deg, var(--silver-dark), var(--white) 45%, var(--silver) 75%, var(--silver-dark));
  }
  .front-contact {
    position: absolute;
    top: 190px;
    left: 0;
    right: 0;
    bottom: 0;
    background: linear-gradient(180deg, var(--navy-mid), var(--navy-deep));
    color: var(--white);
    display: flex;
    flex-direction: column;
    align-items: center;
    justify-content: center;
    gap: 4px;
  }
  .front-contact .phone { font-size: 21px; letter-spacing: 0.5px; }
  .front-contact .web,
  .front-contact .email { font-size: 17px; }

  /* Back side */
  .card-back {
    background: radial-gradient(ellipse at 50% 35%, var(--navy-mid) 0%, var(--navy) 55%, var(--navy-deep) 100%);
    color: var(--white);
  }
  .back-brand {
    position: absolute;
    top: 0;
    left: 0;
    right: 0;
    height: 240px;
    display: flex;
    flex-direction: column;
    align-items: center;
    justify-content: flex-start;
    padding-top: 38px;
  }
  .back-brand .brand-mark {
    width: 54px;
    height: 54px;
    background: linear-gradient(135deg, var(--white), var(--silver-dark));
    margin-bottom: 14px;
  }
  .back-brand .brand-name {
    font-size: 48px;
    color: var(--silver);
    letter-spacing: 1px;
    line-height: 1;
  }
  .back-brand .brand-role {
    margin-top: 8px;
    font-size: 21px;
    color: var(--white);
    letter-spacing: 0.5px;
  }
  .back-slogan {
    position: absolute;
    left: 0;
    right: 0;
    bottom: 34px;
    text-align: center;
    font-size: 15.5px;
    letter-spacing: 1.6px;
    color: var(--white);
  }
</style>
</head>
<body>
  <main class="canvas">
    <section class="card card-front" aria-label="Business card front">
      <div class="front-brand">
        <span class="brand-mark" role="img" aria-label="Brand mark"></span>
        <p class="brand-name">Mira Talwen</p>
        <p class="brand-role">Real Estate Professional</p>
      </div>
      <div class="silver-band"></div>
      <div class="front-contact">
        <p class="phone">301-584-3092</p>
        <p class="web">Bright K Homes.com</p>
        <p class="email">mira@brightkeyhomes.com</p>
      </div>
    </section>

    <section class="card card-back" aria-label="Business card back">
      <div class="back-brand">
        <span class="brand-mark" role="img" aria-label="Brand mark"></span>
        <p class="brand-name">Mira Talwen</p>
        <p class="brand-role">Real Estate Professional</p>
      </div>
      <p class="back-slogan">We simplify your buying and selling real estate</p>
    </section>
  </main>
</body>
</html>
```